We would like to have a poster designed for our new fitness program called " Steady Core Course ". It consists of 1 assessment by a registered physiotherapist and 5 closely monitored exercise sessions. the goal of the program is to develop a strong back to meed the daily demands and sport activities. Ideal program for the people who sit all day for work. Green is our theme color of the clinic. We are open for other colors as well.The poster design should communicate fitness and strength. One time cost of the program is $ 350 . We will see the patient once per week for 6 weeks.

Target Market(s)

People with sitting job and heavy labor job.
Athelets
Active individuals who wanna participate in yoga, running, fitness classes etc.

Industry/Entity Type

Fitness

Font styles to use
Serif

Requirements
Must have
• simplicity and strong message.
Nice to have
• pain free spine picture

```html
<!DOCTYPE html>
<html lang="en">
<head>
<meta charset="utf-8">
<title>Steady Core Course</title>
<link rel="stylesheet" href="https://fonts.googleapis.com/css2?family=Cinzel:wght@400;700;900&family=Merriweather:wght@400;700&display=swap">
<style>
  :root {
    --page-bg: #d9dedd;
    --paper: #f4f4f3;
    --ink: #161616;
    --muted: #3a3a3a;
    --green: #2f7d1f;
    --green-bright: #4aa82e;
    --lime: #8cc63f;
    --bar: #141414;
    --rule: #2a2a2a;
  }
  * { margin: 0; padding: 0; box-sizing: border-box; }
  html, body { width: 1200px; height: 960px; overflow: hidden; }
  body { background: var(--page-bg); position: relative; font-family: "Merriweather", Georgia, serif; color: var(--ink); }

  .poster {
    position: absolute; left: 240px; top: 30px;
    width: 720px; height: 900px;
    background: var(--paper);
    overflow: hidden;
  }

  .brand {
    position: absolute; right: 40px; top: 32px;
    display: flex; align-items: center; gap: 8px;
    font-family: "Merriweather", Georgia, serif; font-weight: 700;
    font-size: 17px; color: var(--green);
  }
  .brand-dot { width: 12px; height: 12px; border-radius: 50%; background: var(--green-bright); }

  .hero-photo {
    position: absolute; left: 250px; top: 55px;
    width: 225px; height: 500px;
    border-radius: 110px 110px 112px 112px;
    background: linear-gradient(180deg, #e9d2bf 0%, #dcbca3 35%, #6a6670 58%, #3fb046 72%, #1f8c2c 92%, #e6e6e5 100%);
  }

  .new-ribbon { position: absolute; left: 205px; top: 500px; width: 90px; height: 100px; }

  .title {
    position: absolute; left: 0; right: 0; top: 568px;
    text-align: center; font-family: "Cinzel", "Times New Roman", serif;
    line-height: 1; padding-left: 20px;
  }
  .title-line { display: block; }
  .title-bold { font-weight: 900; font-size: 56px; color: var(--ink); }
  .title-mid { font-weight: 400; font-size: 50px; color: var(--ink); margin-top: 2px; }
  .title-green { font-weight: 400; font-size: 40px; color: var(--green); margin-top: 4px; }

  .facts {
    position: absolute; left: 68px; right: 40px; top: 752px;
    display: flex;
  }
  .fact { padding: 0 16px; border-left: 1.5px solid var(--rule); }
  .fact:first-child { padding-left: 0; border-left: none; }
  .fact-by { width: 138px; }
  .fact-what { width: 142px; }
  .fact-cost { width: 160px; }
  .fact-time { width: 170px; }
  .fact h3 { font-size: 19px; font-weight: 700; margin-bottom: 6px; color: var(--ink); }
  .fact p { font-size: 13px; line-height: 1.35; color: var(--muted); }
  .fact strong { font-weight: 700; color: var(--ink); }

  .contact-bar {
    position: absolute; left: 0; right: 0; bottom: 0; height: 37px;
    background: var(--bar);
    display: flex; align-items: center; justify-content: center; gap: 12px;
    font-size: 11.5px; color: #ffffff;
  }
  .contact-bar .accent { color: var(--lime); }
</style>
</head>
<body>
  <main class="poster">
    <div class="brand"><span class="brand-dot"></span>Keystone Physio</div>

    <div class="hero-photo" role="img" aria-label="Photo of a woman seen from behind, sitting on a green exercise ball"></div>

    <svg class="new-ribbon" viewBox="0 0 90 100" aria-label="new">
      <polygon points="10,58 62,6 80,24 28,76" fill="#4aa82e"/>
      <polygon points="10,58 28,76 28,96 18,84 10,92" fill="#2f7d1f"/>
      <text x="45" y="47" transform="rotate(-45 45 41)" text-anchor="middle" font-family="Merriweather, serif" font-size="19" font-style="italic" fill="#ffffff">new</text>
    </svg>

    <h1 class="title">
      <span class="title-line title-bold">Steady</span>
      <span class="title-line title-mid">Core</span>
      <span class="title-line title-green">Course</span>
    </h1>

    <section class="facts">
      <div class="fact fact-by">
        <h3>By who?</h3>
        <p>1 assessment by<br>a <strong>Registered<br>Physiotherapist</strong></p>
      </div>
      <div class="fact fact-what">
        <h3>What?</h3>
        <p><strong>5 closely<br>monitored</strong><br>exercise sessions</p>
      </div>
      <div class="fact fact-cost">
        <h3>How much?</h3>
        <p>One time Cost<br>of the Program<br>is <strong>$350</strong></p>
      </div>
      <div class="fact fact-time">
        <h3>How long?</h3>
        <p>See the Patient<br><strong>Once per week<br>for 6 weeks</strong></p>
      </div>
    </section>

    <footer class="contact-bar">
      <span>555.010.2468</span>
      <span class="accent">www.keystonephysio.ca</span>
      <span>keystonephysio@example.com</span>
      <span class="accent">4821-97 street #310 Riverton, AB, Canada</span>
    </footer>
  </main>
</body>
</html>
```